Fast Growing Personal Injury Law Firm Needs Business Card Design

We need a business card design for a fast growing personal injury law firm in Florida. Our name is Darren Kolvisty, P.A. Our practice is comprised of younger attorneys (in their 30s) that employ more modern techniques/tools than our older competition. We would prefer a look that is a modern play on a classic look. Also, we would like to continue using a color scheme that employs navy blue and kelly green (other shades of green could be fine too) as well as our "E" logo.

Industry/Entity Type

Law Firm

```html
<!DOCTYPE html>
<html lang="en">
<head>
<meta charset="utf-8">
<title>Darren Kolvisty, P.A. — Stationery</title>
<link href="https://fonts.googleapis.com/css2?family=Lato:wght@400;700&family=Libre+Baskerville:wght@400;700&display=swap" rel="stylesheet">
<style>
  :root {
    --navy: #1b3a66;
    --navy-name: #24378f;
    --green: #1f8a4c;
    --ink: #2b2b2b;
    --muted: #555;
    --paper: #ffffff;
    --backdrop: #e6e3e1;
  }
  * { box-sizing: border-box; margin: 0; padding: 0; }
  html, body { width: 1200px; height: 1200px; overflow: hidden; }
  body { background: var(--backdrop); font-family: "Lato", sans-serif; color: var(--ink); position: relative; }

  .letterhead { position: absolute; left: 72px; top: 116px; width: 697px; height: 978px; background: var(--paper); overflow: hidden; box-shadow: 0 2px 8px rgba(0,0,0,.12); }
  .brand-mark { position: absolute; background: var(--green); }
  .letterhead .brand-mark { left: 172px; top: 54px; width: 54px; height: 46px; }
  .firm-name { position: absolute; font-family: "Libre Baskerville", serif; font-weight: 700; color: var(--navy-name); white-space: nowrap; }
  .firm-tagline { position: absolute; font-family: "Libre Baskerville", serif; color: var(--green); white-space: nowrap; }
  .letterhead .firm-name { left: 82px; top: 111px; font-size: 27px; }
  .letterhead .firm-tagline { left: 80px; top: 146px; font-size: 17px; letter-spacing: 1.6px; }

  .contact-block { position: absolute; right: 85px; top: 72px; text-align: right; font-size: 10px; line-height: 13px; color: var(--muted); }
  .contact-block .lines { margin-top: 10px; }
  .contact-line { display: flex; justify-content: flex-end; align-items: center; gap: 4px; }
  .dot { display: inline-block; width: 8px; height: 8px; border-radius: 50%; background: var(--navy); }

  .letter-body { position: absolute; left: 85px; top: 229px; width: 541px; font-size: 13px; line-height: 19px; }
  .recipient { font-weight: 700; color: #444; }
  .subject { margin-top: 19px; font-weight: 700; }
  .greeting { margin-top: 14px; }
  .letter-body p.para { margin-top: 12px; }
  .letter-body p.para + p.para { margin-top: 19px; }
  .sign-off { position: absolute; left: 85px; top: 798px; font-size: 13px; line-height: 17px; }
  .signature { display: block; width: 162px; height: 18px; margin: 18px 0 10px; background: linear-gradient(90deg, #d8d8d8, #efefef); border-radius: 3px; }

  .corner-accent { position: absolute; right: 0; bottom: 0; background: linear-gradient(135deg, var(--green), var(--navy)); }
  .letterhead .corner-accent { width: 200px; height: 160px; }

  .card { position: absolute; left: 812px; width: 322px; overflow: hidden; box-shadow: 0 2px 6px rgba(0,0,0,.15); }
  .card-back { top: 180px; height: 180px; background: var(--navy); color: #fff; }
  .card-back .brand-mark { left: 50%; top: 48px; width: 30px; height: 30px; margin-left: -15px; }
  .card-back .firm-name { left: 0; right: 0; top: 90px; text-align: center; color: #fff; font-size: 15px; }
  .card-back .web { position: absolute; left: 0; right: 0; top: 152px; text-align: center; font-size: 8px; }

  .card-front { top: 422px; height: 184px; background: var(--paper); }
  .card-front .brand-mark { left: 17px; top: 20px; width: 34px; height: 26px; }
  .card-front .firm-name { left: 57px; top: 14px; font-size: 16px; }
  .card-front .firm-tagline { left: 57px; top: 35px; font-size: 11px; letter-spacing: .9px; }
  .holder { position: absolute; left: 17px; top: 63px; }
  .holder-name { font-size: 11px; color: var(--navy-name); }
  .holder-title { font-size: 7.5px; color: var(--muted); margin-top: 1px; }
  .card-address { position: absolute; left: 17px; top: 97px; font-size: 7.5px; line-height: 10px; color: var(--muted); }
  .card-contacts { position: absolute; left: 17px; top: 125px; font-size: 7.5px; line-height: 10px; color: var(--muted); }
  .card-contacts .contact-line { justify-content: flex-start; }
  .card-contacts .dot { width: 6px; height: 6px; }
  .card-front .corner-accent { width: 80px; height: 64px; }
</style>
</head>
<body>

<section class="letterhead">
  <span class="brand-mark"></span>
  <div class="firm-name">Darren Kolvisty, P.A.</div>
  <div class="firm-tagline">Personal Injury Attorneys</div>

  <div class="contact-block">
    <div>2150 Harbor Pointe Drive Suite 410</div>
    <div>Palmetto Bay, Florida 33157</div>
    <div class="lines">
      <div class="contact-line">941.555.0142 <span class="dot"></span></div>
      <div class="contact-line">941.555.0178 <span class="dot"></span></div>
      <div class="contact-line">darren@kolvistylaw.com <span class="dot"></span></div>
      <div class="contact-line">www.kolvistylaw.com <span class="dot"></span></div>
    </div>
  </div>

  <div class="letter-body">
    <p class="recipient">Mr. John Doe<br>President</p>
    <p class="subject">Subject: Introduction Letter</p>
    <p class="greeting">Greetings</p>
    <p class="para">Lorem ipsum dolor sit amet, consectetur adipiscing elit. Integer malesuada velit eget venenatis sollicitudin. Nunc molestie pharetra metus. Morbi feugiat elit auctor orci congue, non ultricies est facilisis. Nullam lacinia quis orci non ultrices. Aliquam quam mauris, vulputate eu condimentum non, dictum vel erat. Pellentesque quis odio erat. Duis feugiat, elit vel bibendum malesuada, sem est semper massa, id fermentum diam risus sit amet tortor.</p>
    <p class="para">Pellentesque posuere ut tellus vitae scelerisque. Curabitur sed arcu sit amet lectus porta scelerisque ac eu neque. Nunc dapibus mauris massa, nec auctor odio aliquet a. Nullam eu tempor libero. Nam vitae consequat lectus. Curabitur sed adipiscing velit. Donec non sapien id nulla ornare placerat fringilla sed nisi.</p>
    <p class="para">Mauris orci elit, accumsan nec orci a, feugiat gravida purus. Proin porttitor mattis gravida. Aenean blandit massa dapibus erat porttitor hendrerit. Morbi ut dui justo. Vestibulum felis dui, volutpat ut laoreet eget, gravida a velit. Pellentesque placerat suscipit quam, in mollis elit accumsan id. Curabitur ac suscipit est. Sed fringilla nibh non leo porta rutrum. Vestibulum porta nibh elit, a feugiat sem gravida eu. Nullam in ligula vel mi tincidunt sagittis. Nulla et elementum justo, sed consequat diam. Donec nec semper nibh. Nulla faucibus mauris quis fermentum consequat. Etiam dapibus neque ipsum, id dapibus leo luctus sed. Maecenas ut pulvinar dolor.</p>
    <p class="para">Proin id pulvinar dolor. Praesent posuere purus quis fringilla condimentum. Aenean rhoncus, metus at porta ultrices, nisi velit euismod enim, vitae varius quam velit in mi. Nunc eget rutrum erat. Aenean vel cursus diam. Sed laoreet metus et tortor malesuada, at suscipit neque molestie. Mauris sed malesuada diam, in vulputate metus. In hac habitasse platea dictumst.</p>
  </div>

  <div class="sign-off">
    <p>Regards,</p>
    <span class="signature" role="img" aria-label="Handwritten signature"></span>
    <p>Quentin Adams<br>Executive Director</p>
  </div>

  <div class="corner-accent" role="img" aria-label="Green and navy corner accent"></div>
</section>

<section class="card card-back">
  <span class="brand-mark"></span>
  <div class="firm-name">Darren Kolvisty, P.A.</div>
  <div class="web">www.kolvistylaw.com</div>
</section>

<section class="card card-front">
  <span class="brand-mark"></span>
  <div class="firm-name">Darren Kolvisty, P.A.</div>
  <div class="firm-tagline">Personal Injury Attorneys</div>

  <div class="holder">
    <div class="holder-name">Darren Kolvisty</div>
    <div class="holder-title">Attorney at Law</div>
  </div>

  <div class="card-address">
    <div>2150 Harbor Pointe Drive Suite 410</div>
    <div>Palmetto Bay, Florida 33157</div>
  </div>

  <div class="card-contacts">
    <div class="contact-line"><span class="dot"></span> 941.555.0142</div>
    <div class="contact-line"><span class="dot"></span> 941.555.0178</div>
    <div class="contact-line"><span class="dot"></span> darren@kolvistylaw.com</div>
    <div class="contact-line"><span class="dot"></span> www.kolvistylaw.com</div>
  </div>

  <div class="corner-accent" role="img" aria-label="Green and navy corner accent"></div>
</section>

</body>
</html>
```